PWR Business Card

Looking for a business card for my restaurant group I own. Four different concepts:

Copperleaf Alehouse
Bramble Alehouse
Hollister's Wood Fired Grill
Fenwick Patty Company

Card doesn't need to include all the logos.

```html
<!DOCTYPE html>
<html lang="en">
<head>
<meta charset="utf-8">
<title>PWR Business Card</title>
<link href="https://fonts.googleapis.com/css2?family=Lato:wght@400&family=Montserrat:wght@500;600&display=swap" rel="stylesheet">
<style>
  :root {
    --backdrop: #2a2a2b;
    --slate: #737477;
    --gold: #d3ad6a;
    --paper: #ffffff;
    --ink: #5f6064;
    --rule: #c9c9cb;
  }
  * { box-sizing: border-box; margin: 0; padding: 0; }
  html, body { width: 1200px; height: 1200px; overflow: hidden; }
  body { background: var(--backdrop); position: relative; font-family: "Lato", sans-serif; }

  .card {
    position: absolute; left: 208px; width: 786px; height: 449px;
    border-radius: 26px; overflow: hidden;
  }
  .card--front { top: 126px; background: var(--slate); }
  .card--back { top: 626px; background: var(--paper); }
  .card__band { position: absolute; left: 0; right: 0; bottom: 0; height: 12px; }
  .card--front .card__band { background: var(--gold); }
  .card--back .card__band { background: var(--slate); }

  .brand { position: absolute; left: 0; right: 0; text-align: center;
    font-family: "Montserrat", sans-serif; font-weight: 500; color: var(--gold); }
  .brand__initials { display: block; font-size: 96px; line-height: 1; letter-spacing: 4px; }
  .brand__name { display: block; font-size: 46px; line-height: 1; letter-spacing: 8px; margin-top: 18px; }
  .brand__tagline { display: block; font-size: 22px; line-height: 1; letter-spacing: 4px; margin-top: 12px; }
  .card--front .brand { top: 116px; }
  .card--back .brand { top: 56px; }
  .card--back .brand__initials { font-size: 78px; }
  .card--back .brand__name { font-size: 42px; margin-top: 14px; }
  .card--back .brand__tagline { font-size: 19px; margin-top: 10px; }

  .divider {
    position: absolute; top: 335px; left: 198px; width: 390px; height: 2px;
    background: linear-gradient(90deg, transparent, var(--rule), transparent);
  }
  .venues {
    position: absolute; top: 366px; left: 40px; right: 40px;
    list-style: none; display: flex; flex-wrap: wrap; justify-content: center;
    column-gap: 22px; row-gap: 8px;
    color: var(--paper); font-size: 18px; letter-spacing: 0.8px; line-height: 21px;
  }
  .venues li { display: flex; align-items: center; gap: 10px; }
  .venues li::before { content: ""; width: 9px; height: 9px; border-radius: 50%; background: var(--gold); }
  .venues .venue--last { margin: 0 160px; }

  .person { position: absolute; top: 300px; right: 440px; text-align: right; }
  .person__name { font-family: "Montserrat", sans-serif; font-weight: 600; color: var(--gold);
    font-size: 33px; line-height: 1; }
  .person__role { color: var(--ink); font-size: 20px; letter-spacing: 0.8px; margin-top: 8px; }
  .contact-rule { position: absolute; left: 373px; top: 296px; width: 2px; height: 74px; background: var(--ink); }
  .contacts { position: absolute; left: 394px; top: 290px; list-style: none;
    color: var(--ink); font-size: 21px; letter-spacing: 0.6px; }
  .contacts li { display: flex; align-items: center; gap: 12px; height: 29px; }
  .contacts svg { width: 18px; height: 18px; fill: var(--gold); flex: none; }
</style>
</head>
<body>
  <section class="card card--front">
    <div class="brand">
      <span class="brand__initials">PWR</span>
      <span class="brand__name">PINEWOOD</span>
      <span class="brand__tagline">HOSPITALITY GROUP</span>
    </div>
    <div class="divider"></div>
    <ul class="venues">
      <li>Copperleaf Alehouse</li>
      <li>Bramble Alehouse</li>
      <li>Hollister's Wood Fired Grill</li>
      <li class="venue--last">Fenwick Patty Company</li>
    </ul>
    <div class="card__band"></div>
  </section>

  <section class="card card--back">
    <div class="brand">
      <span class="brand__initials">PWR</span>
      <span class="brand__name">PINEWOOD</span>
      <span class="brand__tagline">HOSPITALITY GROUP</span>
    </div>
    <div class="person">
      <div class="person__name">MAREN WHITLOCK</div>
      <div class="person__role">Owner</div>
    </div>
    <div class="contact-rule"></div>
    <ul class="contacts">
      <li>
        <svg viewBox="0 0 24 24" aria-hidden="true"><path d="M6.6 10.8a15.2 15.2 0 0 0 6.6 6.6l2.2-2.2a1 1 0 0 1 1-.25 11.4 11.4 0 0 0 3.6.57 1 1 0 0 1 1 1V20a1 1 0 0 1-1 1A17 17 0 0 1 3 4a1 1 0 0 1 1-1h3.5a1 1 0 0 1 1 1c0 1.25.2 2.45.57 3.57a1 1 0 0 1-.25 1z"/></svg>
        555.014.2290
      </li>
      <li>
        <svg viewBox="0 0 24 24" aria-hidden="true"><path d="M2 5h20v14H2z M3.5 6.5 12 13l8.5-6.5" stroke="#fff" stroke-width="1.5"/></svg>
        marenwhitlock@mailbox.com
      </li>
      <li>
        <svg viewBox="0 0 24 24" aria-hidden="true"><circle cx="12" cy="12" r="9.5" fill="none" stroke="#d3ad6a" stroke-width="1.6"/><path d="M2.5 12h19M12 2.5c-5 5-5 14 0 19M12 2.5c5 5 5 14 0 19M4 7.5h16M4 16.5h16" fill="none" stroke="#d3ad6a" stroke-width="1.4"/></svg>
        www.pinewoodhospitality.com
      </li>
    </ul>
    <div class="card__band"></div>
  </section>
</body>
</html>
```